A reimagined website for a cross-border tax firm

There are two aspects to this project for Brindlemoor Tax Advisory:
1) I need a logo update to accommodate increasing focus and specialization in my business. The byline under the name “Brindlemoor Tax Advisory” needs to change:
ORIGINAL: TAX SUPPORT FOR PUBLIC ACCOUNTING FIRMS
REVISED: CROSS-BORDER TAX SERVICES • U.S. & CANADA
2) I need a website “refresh” (see current website at www.levyhelpdesk.example) based on this logo – a new vision for a website with greater clarity, focus and organization. It should represent a re-envisioning of the current approach, and not the wholesale abandonment of the style represented there. I need it to be creative, compelling and attention grabbing, but still professional. This should, at a minimum, update any places where the old name/logo is used, but I want the redesign to go beyond this to something more intuitive. I need high quality separate PNG files of the various logo styles for use in various documents, but HTML coding would be a helpful but not necessary addition.

Target Market(s)

People in need of cross-border tax services - Canada and US

Coding

Number of Pages Required

Requirements
Must have
• Greater crispness, sharpness - higher resolution
• A more compelling, organized approach - make the wording and images more accessible to the website user (especially the staff bios, which have scroll bars now)
Nice to have
• Replacement of stock image with a true image of the Halifax skyline
Should not have
• Deviate from colour pattern represented in website logo of blue/orange
• Deviate from existing logo except for word replacement

```html
<!DOCTYPE html>
<html lang="en">
<head>
<meta charset="utf-8">
<title>Brindlemoor Tax Advisory</title>
<link rel="stylesheet" href="https://fonts.googleapis.com/css2?family=Poppins:wght@600;700&family=Montserrat:wght@300;400;500;600&family=Lora:wght@400;700&display=swap">
<style>
:root{
  --navy:#2b2f6a;
  --navy-deep:#232656;
  --footer:#33356a;
  --footer-bar:#2d2f60;
  --hero-a:#2a3d8c;
  --hero-b:#3a5cb0;
  --ink:#1d2c8f;
  --accent:#16b4e8;
  --orange:#f2892a;
  --muted:#8a8fa8;
  --white:#ffffff;
}
*{margin:0;padding:0;box-sizing:border-box}
html,body{width:1200px;height:2485px;overflow:hidden;background:var(--white)}
.page{position:relative;width:1200px;height:2485px;overflow:hidden;font-family:"Lora",serif;color:var(--muted)}
.abs{position:absolute}
.hero{left:0;top:0;width:1200px;height:603px;background:linear-gradient(160deg,var(--hero-a),var(--hero-b) 70%,#4a72c4)}
.hero-portrait{left:532px;top:133px;width:498px;height:395px;background:linear-gradient(180deg,#6f96d6,#9cc1ea 60%,#4f7ac4)}
.nav{left:196px;top:45px;width:808px;height:85px;background:#1b1f4a;display:flex;align-items:center;padding:0 0 0 22px}
.brand{display:flex;align-items:center;gap:9px;font-family:"Montserrat",sans-serif;font-weight:600;font-size:16px;color:var(--accent);white-space:nowrap}
.brand-mark{width:16px;height:16px;background:var(--orange)}
.menu{display:flex;gap:24px;margin-left:auto;margin-right:130px;list-style:none;font-family:"Montserrat",sans-serif;font-size:12px;color:#c7cbe6;white-space:nowrap}
.menu li{display:flex;align-items:center;gap:8px}
.menu li::before{content:"";width:6px;height:6px;border:1.5px solid var(--accent);border-radius:50%}
.menu .current{color:var(--white)}
.buy{left:911px;top:70px;width:79px;height:31px;background:var(--accent);color:var(--white);font-family:"Montserrat",sans-serif;font-size:12px;display:flex;align-items:center;justify-content:center}
.hero-title{left:216px;top:228px;font-family:"Poppins",sans-serif;font-weight:700;font-size:46px;line-height:63px;color:var(--white)}
.link{display:flex;align-items:center;gap:12px;font-family:"Lora",serif;font-weight:700;font-size:15px;color:var(--accent)}
.link span{border-bottom:2px solid var(--accent);padding-bottom:5px}
.link svg{width:9px;height:12px}
.hero-link{left:216px;top:500px}
.address-panel{left:0;top:603px;width:482px;height:575px;background:linear-gradient(180deg,var(--navy),#262a5e)}
.address-rule{left:206px;top:660px;width:77px;height:3px;background:var(--orange)}
.address{left:206px;top:696px;font-family:"Montserrat",sans-serif;font-size:23px;line-height:30px;color:var(--white)}
.count-big{left:206px;top:800px;font-family:"Montserrat",sans-serif;font-weight:300;font-size:52px;color:#aab0d6}
.address-note{left:206px;top:890px;width:230px;font-size:10.5px;line-height:15px;color:#9ca2cf}
.why{left:482px;top:528px;width:718px;height:650px;background:var(--white)}
.eyebrow{font-family:"Montserrat",sans-serif;font-size:10.5px;letter-spacing:3px;color:var(--ink);text-transform:uppercase}
.why-label{left:613px;top:588px}
.reason{left:540px;width:440px;display:flex;gap:34px}
.reason-num{flex:none;width:40px;height:40px;border-radius:50%;border:1.5px solid #d5d8e6;border-left-color:var(--accent);display:flex;align-items:center;justify-content:center;font-family:"Montserrat",sans-serif;font-size:13px;color:var(--ink);margin-top:4px}
.reason h3{font-family:"Montserrat",sans-serif;font-weight:500;font-size:18.5px;color:var(--ink);margin-bottom:8px}
.reason p{font-size:10.5px;line-height:16px;color:var(--muted);width:330px}
.learn{left:618px;top:964px}
.band{left:868px;top:1178px;width:332px;height:374px;background:var(--navy)}
.meeting-photo{left:194px;top:1104px;width:674px;height:448px;background:linear-gradient(135deg,#34406a,#8b9a8a 45%,#d9dbe0 70%,#b7c2cf);box-shadow:0 20px 40px rgba(30,34,80,.18)}
.feature-card{left:248px;top:1373px;width:372px;height:179px;background:var(--white);padding:32px 26px;box-shadow:0 10px 30px rgba(30,34,80,.15)}
.feature-card h2{font-family:"Montserrat",sans-serif;font-weight:500;font-size:24px;line-height:28px;color:var(--ink);margin:12px 0 20px}
.staff-label{left:193px;top:1634px}
.staff-title{left:193px;top:1658px;font-family:"Montserrat",sans-serif;font-weight:500;font-size:35px;line-height:41px;color:var(--ink)}
.scales{left:765px;top:1612px;width:290px;height:407px;background:radial-gradient(ellipse at 50% 45%,#e8c766,#c9a13c 45%,rgba(255,255,255,0) 72%)}
.member{top:1825px;width:190px}
.avatar{width:110px;height:110px;border-radius:50%;background:linear-gradient(160deg,#4a4d57,#9c8f86);margin-left:1px}
.member h4{font-family:"Montserrat",sans-serif;font-weight:500;font-size:15px;color:var(--ink);margin:22px 0 0 24px}
.member .role{font-family:"Montserrat",sans-serif;font-size:11.5px;color:var(--ink);margin:4px 0 0 24px}
.member p{font-size:10px;line-height:15px;margin:14px 0 0 24px;width:160px}
.staff-rule{left:194px;top:2098px;width:607px;height:2px;background:#bfe7f6}
.staff-count{left:210px;top:2126px;font-family:"Montserrat",sans-serif;font-weight:500;font-size:46px;color:var(--ink)}
.staff-count-note{left:297px;top:2140px;width:150px;font-size:9.5px;line-height:14px}
.see-staff{left:612px;top:2140px}
.footer{left:0;top:2207px;width:1200px;height:220px;background:var(--footer)}
.footer-bar{left:0;top:2427px;width:1200px;height:58px;background:var(--footer-bar);border-top:1px solid #3f4277}
.foot-title{font-family:"Montserrat",sans-serif;font-weight:400;font-size:18px;line-height:23px;color:var(--white)}
.foot-left{left:194px;top:2234px}
.foot-mid{left:525px;top:2234px}
.foot-btn{left:194px;top:2333px;width:106px;height:31px;background:var(--accent);color:var(--white);font-size:10.5px;display:flex;align-items:center;justify-content:center}
.foot-list{list-style:none;font-size:9.5px;color:#b6b9dc}
.foot-list li{height:26.6px;display:flex;align-items:center;gap:12px}
.foot-list li::before{content:"\2192";color:var(--accent)}
.col-a{left:525px;top:2305px}
.col-b{left:655px;top:2305px}
.building-box{left:889px;top:2243px;width:115px;height:162px;background:#5a5d94}
.copy{left:194px;top:2452px;font-size:9.5px;color:#9a9dc6}
.socials{left:884px;top:2452px;display:flex;gap:14px}
.socials i{width:9px;height:9px;border-radius:50%;background:#8f93c2;display:block}
.top-btn{left:982px;top:2450px}
</style>
</head>
<body>
<div class="page">

  <section class="abs hero" role="img" aria-label="Office interior in blue tones"></section>
  <div class="abs hero-portrait" role="img" aria-label="Smiling tax advisor holding glasses"></div>

  <nav class="abs nav">
    <div class="brand"><span class="brand-mark"></span>Brindlemoor Tax Advisory</div>
    <ul class="menu">
      <li class="current">Home</li><li>About</li><li>Info</li><li>Treatment</li><li>Contact</li>
    </ul>
  </nav>
  <div class="abs buy">Buy now</div>

  <h1 class="abs hero-title">Cross-Border Tax<br>Services &bull; U.S.<br>&amp; Canada</h1>
  <a class="abs link hero-link"><svg viewBox="0 0 9 12"><path d="M2 1l5 5-5 5" fill="none" stroke="currentColor" stroke-width="2"/></svg><span>Read more</span></a>

  <section class="abs address-panel" role="img" aria-label="City building facade in navy"></section>
  <div class="abs address-rule"></div>
  <p class="abs address">14 Wexford Lane<br>Harrowgate Quay<br>London</p>
  <p class="abs count-big">172</p>
  <p class="abs address-note">Vivamus in diam turpis. In condimentum maximus tristique. Maecenas non laoreet odio. Fusce lobortis porttitor purus, vel vestibulum libero pharetra vel. Pellentesque lorem augue.</p>

  <section class="abs why"></section>
  <p class="abs eyebrow why-label">Why to choose us</p>
  <div class="abs reason" style="top:648px"><div class="reason-num">1</div><div><h3>Based on true care and passion</h3><p>Lorem ipsum dolor sit amet, consectetur adipiscing elit. Nulla mauris dolor, gravida a varius blandit, auctor eget purus. Phasellus scelerisque sapien.</p></div></div>
  <div class="abs reason" style="top:753px"><div class="reason-num">2</div><div><h3>Experienced staff</h3><p>Lorem ipsum dolor sit amet, consectetur adipiscing elit. Nulla mauris dolor, gravida a varius blandit, auctor eget purus. Phasellus scelerisque sapien.</p></div></div>
  <div class="abs reason" style="top:859px"><div class="reason-num">3</div><div><h3>Best possible equipment</h3><p>Lorem ipsum dolor sit amet, consectetur adipiscing elit. Nulla mauris dolor, gravida a varius blandit, auctor eget purus. Phasellus scelerisque sapien.</p></div></div>
  <a class="abs link learn"><svg viewBox="0 0 9 12"><path d="M2 1l5 5-5 5" fill="none" stroke="currentColor" stroke-width="2"/></svg><span>Learn more details</span></a>

  <div class="abs band"></div>
  <div class="abs meeting-photo" role="img" aria-label="Advisors reviewing documents with a calculator at a desk"></div>
  <article class="abs feature-card">
    <p class="eyebrow">Gravida</p>
    <h2>Lorem sum dolor<br>sit amet enim ullamcor</h2>
    <a class="link"><svg viewBox="0 0 9 12"><path d="M2 1l5 5-5 5" fill="none" stroke="currentColor" stroke-width="2"/></svg><span style="font-weight:400;font-size:12px">Read more</span></a>
  </article>

  <p class="abs eyebrow staff-label">Our staff</p>
  <h2 class="abs staff-title">We hire only<br>the most experienced<br>specialists</h2>
  <div class="abs scales" role="img" aria-label="Golden scales of justice"></div>

  <div class="abs member" style="left:191px"><div class="avatar" role="img" aria-label="Portrait of Callum Reyes"></div><h4>Callum</h4><p class="role">Reyes, CPA, CGA, EA</p><p>Duis dignissim mi ut laoreet mollis. Nunc id tellus finibus, eleifend mi vel, maximus justo. Maecenas mi tortor.</p></div>
  <div class="abs member" style="left:399px"><div class="avatar" role="img" aria-label="Portrait of Martin Oakhurst"></div><h4>Martin</h4><p class="role">Oakhurst, CPA, CA</p><p>Curabitur sed iaculis dolor, non congue ligula. Maecenas imperdiet ante eget hendrerit posuere. Nunc urna.</p></div>
  <div class="abs member" style="left:603px"><div class="avatar" role="img" aria-label="Portrait of Nadia Fenwick"></div><h4>Nadia</h4><p class="role">Fenwick</p><p>Sed ultrices nisl velit, eu ornare est ullamcorper a. Nunc quis nibh magna. Proin risus erat, fringilla vel purus sit.</p></div>

  <div class="abs staff-rule"></div>
  <p class="abs staff-count">42</p>
  <p class="abs staff-count-note">Curabitur sed iaculis dolor, non congue ligula. Maecenas</p>
  <a class="abs link see-staff"><svg viewBox="0 0 9 12"><path d="M2 1l5 5-5 5" fill="none" stroke="currentColor" stroke-width="2"/></svg><span style="border:0;font-size:12px">See the whole staff</span></a>

  <footer class="abs footer"></footer>
  <h3 class="abs foot-title foot-left">Vestibulum dapibus,<br>mauris nec malesuada<br>fames ac turpis velit</h3>
  <div class="abs foot-btn">View more details</div>
  <h3 class="abs foot-title foot-mid">Nullam wisi ultricies a<br>gravida vitae</h3>
  <ul class="abs foot-list col-a"><li>Aenean solli</li><li>Duis sed odio sit</li><li>Morbi accumsan</li><li>Nam nec tellus</li></ul>
  <ul class="abs foot-list col-b"><li>Duis sed odio</li><li>Morbi accum</li><li>Nam nec</li><li>Class aptent</li></ul>
  <div class="abs building-box" role="img" aria-label="Line drawing of a house facade"></div>

  <div class="abs footer-bar"></div>
  <p class="abs copy">© 2017 Brindlemoor - All Rights Reserved.</p>
  <div class="abs socials"><i></i><i></i><i></i><i></i></div>
  <svg class="abs top-btn" width="12" height="8" viewBox="0 0 12 8"><path d="M1 7l5-5 5 5" fill="none" stroke="#8f93c2" stroke-width="1.5"/></svg>

</div>
</body>
</html>
```